Web Developer Wordpress theme

I'm a web developer but a poor designer so i need somebody to design me a cool and professional WordPress theme. I specialize in shopping cart developments and modifications as well as hosting for these system so would like the design to show this off. I am UK based and want this to also come across in the design.
As for colors and layout i am open mined just use your imaginantion i will let know what i think of your designs.
also forgot to mention my business name is travolek
and my exsiting site is travolek.co.uk

```html
<!DOCTYPE html>
<html lang="en">
<head>
<meta charset="utf-8">
<title>travolek – serious web development</title>
<link href="https://fonts.googleapis.com/css2?family=Arimo:ital,wght@0,400;0,700;1,400&family=Open+Sans:wght@400;600&family=Oswald:wght@700&display=swap" rel="stylesheet">
<style>
:root{
  --dark:#262626;
  --dark-2:#1e1e1e;
  --blue:#1b74f2;
  --blue-deep:#0d5ee0;
  --blue-link:#1a78ee;
  --orange:#ff8a00;
  --orange-light:#ffb000;
  --grey-bg:#f1f2f4;
  --card:#ffffff;
  --text:#555;
  --text-dark:#333;
  --quote-bg:#e6e7e9;
  --green:#3bb54a;
  --footer-text:#c9c9c9;
  --footer-line:#3d3d3d;
}
*{margin:0;padding:0;box-sizing:border-box}
html,body{width:882px;height:1200px;overflow:hidden}
body{position:relative;font-family:"Arimo",Arial,sans-serif;color:var(--text);background:var(--grey-bg)}
a{text-decoration:none;color:inherit}
.abs{position:absolute}

/* header */
.top-band{left:0;top:0;width:882px;height:144px;background:var(--dark);border-top:6px solid var(--blue)}
.account-tab{left:574px;top:6px;width:128px;height:21px;background:var(--blue);border-radius:0 0 6px 6px;font-size:9px;color:#fff;display:flex;align-items:center;justify-content:center;gap:6px}
.account-tab .dot{width:10px;height:10px;border-radius:50%;background:#e8e8e8}
.account-tab .register{color:#ffd84a}
.brand{left:140px;top:50px;display:flex;align-items:center;gap:8px}
.brand-mark{width:26px;height:26px;border-radius:50%;background:var(--blue)}
.brand-name{font-family:"Arimo",Arial,sans-serif;font-size:40px;color:var(--orange);letter-spacing:-1px;line-height:1}
.brand-tag{left:197px;top:100px;font-size:7px;font-weight:700;color:#e0e0e0;letter-spacing:1.2px}

.hero{left:0;top:144px;width:882px;height:376px;background:linear-gradient(180deg,#1570f3 0%,#1f7cfb 60%,#2a86ff 100%)}
.nav{left:104px;top:124px;width:658px;height:38px;background:#fff;border-radius:19px;box-shadow:0 2px 4px rgba(0,0,0,.25);display:flex;align-items:center;padding-left:17px;font-size:10px;color:var(--text-dark)}
.nav a{margin-right:21px}
.nav .current{background:var(--orange);color:#fff;border-radius:12px;padding:5px 17px;border:1px solid #e07000;margin-right:20px}
.search{position:absolute;left:491px;top:10px;width:148px;height:19px;border:1px solid #d5d5d5;border-radius:8px;font-size:8px;font-style:italic;color:#999;padding:4px 8px}
.search svg{position:absolute;right:7px;top:4px}

.slider-art{left:160px;top:216px;width:332px;height:232px;border-radius:4px;background:linear-gradient(180deg,#1c2530 0%,#2f3d4a 50%,rgba(40,90,200,.4) 100%)}
.arrow{width:19px;height:19px;border-radius:50%}
.arrow.prev{left:127px;top:287px;background:#fff}
.arrow.next{left:499px;top:287px;background:var(--orange)}
.hero-title{left:534px;top:198px;font-size:20px;color:#fff;line-height:19px;font-weight:400}
.hero-copy{left:537px;top:277px;width:191px;font-size:9.4px;line-height:12.4px;color:#fff;text-align:justify}
.cta{left:585px;top:404px;width:145px;height:44px;background:linear-gradient(180deg,var(--orange-light),var(--orange));border:1px solid #e07800;border-radius:3px;font-family:"Oswald",sans-serif;font-size:21px;color:#5a2a00;display:flex;align-items:center;justify-content:center;box-shadow:0 4px 4px rgba(0,0,0,.2)}

/* service cards */
.card{top:480px;width:206px;height:134px;background:var(--card);border:1px solid #ddd;border-radius:4px;box-shadow:0 6px 6px -4px rgba(0,0,0,.25);padding:0 9px}
.card-icon{position:absolute;left:10px;top:10px;width:40px;height:40px;border-radius:6px}
.card h3{position:absolute;left:58px;top:24px;font-size:11px;font-weight:400;color:var(--text-dark)}
.card .sub{position:absolute;left:58px;top:39px;font-size:8.4px;font-style:italic;color:var(--blue-link)}
.card p{position:absolute;left:10px;top:62px;width:187px;font-size:8.2px;line-height:12.4px;text-align:justify}
.card p span{color:var(--blue-link)}
.more{position:absolute;right:16px;bottom:10px;font-size:8px;color:var(--blue-link);display:flex;align-items:center;gap:5px}
.more i{width:10px;height:10px;border-radius:50%;background:var(--orange-light);display:inline-block}

/* info columns */
.col-head{font-size:13px;color:var(--text-dark);font-family:"Open Sans",sans-serif}
.col-head b{color:var(--blue-link);font-weight:400}
.col-sub{font-size:8.6px;font-style:italic;color:var(--blue-link)}
.body-copy{font-size:8.4px;line-height:12.4px;text-align:justify}
.btn{height:18px;border-radius:3px;background:linear-gradient(180deg,var(--orange-light),var(--orange));border:1px solid #e07800;color:#fff;font-size:8px;display:flex;align-items:center;justify-content:center}
.checks{list-style:none;font-size:8.4px}
.checks li{position:absolute;left:0;display:flex;align-items:center;gap:8px;white-space:nowrap}
.checks i{width:9px;height:9px;border-radius:50%;background:var(--green);display:inline-block}
.quote{left:558px;width:207px;height:52px;background:var(--quote-bg);font-size:8.4px;font-style:italic;line-height:12.4px;text-align:justify;padding:4px 8px}
.quote-by{font-size:8.4px;font-style:italic}
.quote-by a{color:var(--blue-link)}

/* footer */
.footer{left:0;top:940px;width:882px;height:260px;background:var(--dark);border-top:6px solid var(--blue)}
.f-head{font-family:"Open Sans",sans-serif;font-size:13px;color:var(--orange);display:flex;align-items:center;gap:7px}
.f-list{list-style:none;font-size:8.2px;color:var(--footer-text)}
.f-list li{height:20.7px;border-bottom:1px solid var(--footer-line);padding:4px 9px;letter-spacing:.3px}
.blog li{height:34px;padding:3px 8px}
.blog small{display:block;font-style:italic;color:#777;font-size:8px}
.map{left:602px;top:1002px;width:120px;height:84px;border:2px solid #555;background:linear-gradient(135deg,#f3e3b8,#e9d9a6 50%,#d8d0b8)}
.address{left:594px;top:1096px;width:140px;text-align:center;font-size:8.2px;color:var(--footer-text);line-height:11.6px}
.address a{color:var(--blue-link);display:block;margin-top:3px}
.social{top:1118px;width:22px;height:22px;border-radius:50%;background:#f2f2f2;border:2px solid #ccc}
.copyright{left:0;top:1158px;width:882px;text-align:center;font-size:8.2px;color:var(--footer-text);letter-spacing:.4px}
</style>
</head>
<body>

<header>
  <div class="abs top-band"></div>
  <div class="abs account-tab"><a href="#">Login</a><span class="dot"></span><span>I</span><a class="register" href="#">Register</a></div>
  <div class="abs brand"><span class="brand-mark"></span><span class="brand-name">travolek</span></div>
  <div class="abs brand-tag">serious web developement</div>
</header>

<section class="abs hero"></section>

<nav class="abs nav">
  <a class="current" href="#">Home</a>
  <a href="#">About Us</a><a href="#">Addons</a><a href="#">Work</a><a href="#">Services</a><a href="#">Blogs</a><a href="#">Contact Us</a>
  <div class="search">search here....
    <svg width="11" height="11" viewBox="0 0 11 11"><circle cx="4.5" cy="4.5" r="3.2" fill="none" stroke="#1a78ee" stroke-width="1.5"/><line x1="7" y1="7" x2="10" y2="10" stroke="#1a78ee" stroke-width="1.8"/></svg>
  </div>
</nav>

<div class="abs slider-art" role="img" aria-label="Fanned row of website screenshots with reflection"></div>
<svg class="abs arrow prev" viewBox="0 0 19 19"><path d="M11 5 L7 9.5 L11 14" fill="none" stroke="#333" stroke-width="2"/></svg>
<svg class="abs arrow next" viewBox="0 0 19 19"><path d="M8 5 L12 9.5 L8 14" fill="none" stroke="#fff" stroke-width="2"/></svg>

<h1 class="abs hero-title">We create beautiful<br>websites and graphics<br>for the web!</h1>
<p class="abs hero-copy">We like to offer you the complete package here at travolek, so when you order a shopping cart from us we like to make your you get the hosting required to handle the data so your site never sees any problems. We use a reliable secure data center to host our servers. We also can offer you a SSL certificate so you can keep all your data communications secure too.</p>
<a class="abs cta" href="#">VIEW MORE</a>

<article class="abs card" style="left:118px">
  <div class="card-icon" role="img" aria-label="Paint brushes and palette" style="background:linear-gradient(135deg,#d9d9d9,#8a8a8a)"></div>
  <h3>Web Design</h3><div class="sub">Start from £ 400 with all sevices</div>
  <p>Lorem ipsum dolor sit amet, tempor invidunt ut labore et dolore magna aliquyam erat, sed diam voluptua. <span>At vero eos et accusam</span> et justo duo diam nonumy eirmod.</p>
  <a class="more" href="#">Learn More <i></i></a>
</article>
<article class="abs card" style="left:341px">
  <div class="card-icon" role="img" aria-label="Folder with globe" style="background:linear-gradient(135deg,#ffd23a,#2d8fe0)"></div>
  <h3>Web Development</h3><div class="sub">Start from £ 500 GUARANTED</div>
  <p>Lorem ipsum dolor sit amet, consetetur sadipscing elitr, sed diam <span>nonumy eirmod</span> tempor invidunt ut labore et dolore magna aliquyam erat, sed diam voluptua.</p>
  <a class="more" href="#">Lean More <i></i></a>
</article>
<article class="abs card" style="left:558px">
  <div class="card-icon" role="img" aria-label="Server racks" style="background:linear-gradient(180deg,#5a6068,#1f2326)"></div>
  <h3>e-Commerce Hosting</h3><div class="sub">Up to 2 TB storage spaces</div>
  <p>Lorem ipsum dolor sit amet, consetetur sadipscing elitr, sed diam nonumy <span>eirmod tempor</span> invidunt ut labore et dolore magna aliquyam duo.</p>
  <a class="more" href="#">Learn More <i></i></a>
</article>

<!-- info columns -->
<section>
  <span class="abs" style="left:118px;top:664px;width:30px;height:30px;border-radius:50%;background:var(--blue)"></span>
  <h2 class="abs col-head" style="left:155px;top:664px">What’s <b>Travolek</b>?</h2>
  <div class="abs col-sub" style="left:157px;top:683px">Why you must chose us</div>
  <p class="abs body-copy" style="left:119px;top:707px;width:203px">Sestibulum ante ipsum primis in faucibus orci luctus et ultrices posuere cubilia Curae; Morbi commodo mattis Lorem ipsum dolor sit amet, consectetur adipiscing elit. Fusce sed neque justo. Nam a metus augue, nec pharetra mi. Nulla nisi libero, luctus vel ullamcorper rutrum, porta sed tellus.</p>
  <p class="abs body-copy" style="left:119px;top:794px;width:203px">Proin non congue arcu. Suspendisse potenti. Vestibulum ante ipsum primis in faucibus orci luctus et ultrices posuere cubilia Curae.</p>
  <a class="abs btn" href="#" style="left:258px;top:844px;width:64px">Read more</a>

  <div class="abs" role="img" aria-label="Globe with gear" style="left:342px;top:665px;width:35px;height:35px;border-radius:50%;background:radial-gradient(circle at 35% 35%,#9fd3ff,#1a6fd6)"></div>
  <h2 class="abs col-head" style="left:388px;top:663px">Our <b>Services</b></h2>
  <div class="abs col-sub" style="left:388px;top:683px">Nam liber tempor cum soluta</div>
  <p class="abs body-copy" style="left:339px;top:706px;width:205px;text-align:left">Duis autem vel eum iriure dolor in hendrerit in vulputate velit esse molestie consequat.</p>
  <ul class="abs checks" style="left:356px;top:0">
    <li style="top:740px"><i></i>Website Design and Progamming</li>
    <li style="top:765px"><i></i>Web Development</li>
    <li style="top:790px"><i></i>Content Management System</li>
    <li style="top:815px"><i></i>E-mail Marketing</li>
    <li style="top:840px"><i></i>Search Engine Optimation (SEO)</li>
  </ul>
  <a class="abs btn" href="#" style="left:478px;top:868px;width:64px">Detail</a>

  <svg class="abs" style="left:558px;top:662px" width="42" height="34" viewBox="0 0 42 34"><ellipse cx="15" cy="12" rx="14" ry="10" fill="#9cc9f2" stroke="#3a88d8" stroke-width="1.5"/><ellipse cx="26" cy="20" rx="14" ry="10" fill="#d8ecff" stroke="#3a88d8" stroke-width="1.5"/><path d="M30 29 L34 34 L34 28z" fill="#3a88d8"/></svg>
  <h2 class="abs col-head" style="left:610px;top:663px">Customers <b>Say</b></h2>
  <div class="abs col-sub" style="left:610px;top:683px">Nam liber tempor cum soluta</div>
  <blockquote class="abs quote" style="top:708px">“Praesent lorem libero, porta et porta at, imperdiet eget neque. Nunc aliquam vestibulum fermentum. Nunc elementum auctor sodales.”</blockquote>
  <div class="abs quote-by" style="left:628px;top:774px">- John Doe, <a href="#">Web Progammer</a> -</div>
  <blockquote class="abs quote" style="top:792px">“Praesent lorem libero, porta et porta at, imperdiet eget neque. Nunc aliquam vestibulum fermentum. Nunc elementum auctor sodales.”</blockquote>
  <div class="abs quote-by" style="left:628px;top:858px">- John Doe, <a href="#">Web Progammer</a> -</div>
  <a class="abs btn" href="#" style="left:702px;top:877px;width:63px">Read more</a>
</section>

<footer class="abs footer"></footer>

<h3 class="abs f-head" style="left:138px;top:968px"><svg width="14" height="18" viewBox="0 0 14 18"><path d="M7 0a7 7 0 0 0-7 7c0 5 7 11 7 11s7-6 7-11a7 7 0 0 0-7-7z" fill="#fff"/><circle cx="7" cy="7" r="2.5" fill="#262626"/></svg>Navigation</h3>
<ul class="abs f-list" style="left:137px;top:991px;width:102px;border-top:1px solid var(--footer-line)">
  <li>Log In</li><li>Sign Up</li><li>Privacy of Policy</li><li>Get in touch</li>
</ul>
<h3 class="abs f-head" style="left:138px;top:1089px">Follow</h3>
<span class="abs social" style="left:138px"></span>
<span class="abs social" style="left:172px"></span>
<span class="abs social" style="left:206px"></span>

<h3 class="abs f-head" style="left:270px;top:967px"><svg width="20" height="14" viewBox="0 0 20 14"><rect x="1" y="3" width="10" height="8" rx="4" fill="none" stroke="#fff" stroke-width="2" transform="rotate(-30 6 7)"/><rect x="9" y="3" width="10" height="8" rx="4" fill="none" stroke="#fff" stroke-width="2" transform="rotate(-30 14 7)"/></svg>Links</h3>
<ul class="abs f-list" style="left:268px;top:991px;width:102px">
  <li>Searchly.com</li><li>ThemeMarket.net</li><li>GraphicHub</li><li>LayerTuts</li><li>ModelBay</li><li>ScriptVault</li>
</ul>

<h3 class="abs f-head" style="left:390px;top:967px"><svg width="22" height="18" viewBox="0 0 22 18"><path d="M1 6h5l11-5v16L6 12H1z" fill="#fff"/><rect x="4" y="12" width="4" height="6" fill="#fff"/></svg>From the Blog</h3>
<ul class="abs f-list blog" style="left:388px;top:990px;width:187px;border-top:1px solid var(--footer-line)">
  <li>HTML5 &amp; CSS3 : Pros &amp; Cons<small>by John Doe &nbsp;&nbsp;&nbsp;&nbsp;55 Comments</small></li>
  <li>Hosting &amp; Domain Free 100%<small>by John Doe &nbsp;&nbsp;&nbsp;&nbsp;15 Comments</small></li>
  <li>Guaranteed Project with Us<small>by John Doe &nbsp;&nbsp;&nbsp;&nbsp;15 Comments</small></li>
</ul>

<h3 class="abs f-head" style="left:594px;top:966px"><svg width="26" height="18" viewBox="0 0 26 18"><path d="M1 6c0-4 24-4 24 0v3h-6V6H7v3H1z" fill="#fff"/><rect x="5" y="9" width="16" height="9" rx="2" fill="#fff"/><circle cx="13" cy="13.5" r="2.5" fill="#262626"/></svg>Find Us</h3>
<div class="abs" style="left:594px;top:990px;width:158px;border-top:1px solid var(--footer-line)"></div>
<div class="abs map" role="img" aria-label="Street map showing the office location"></div>
<address class="abs address" style="font-style:normal">Sample street 3444 - London<br>Sample Country 55261<a href="#">View large map &gt;</a></address>

<p class="abs copyright">Copyright © 2011 travolek.co.uk - All rights reserved. Managed by travolek &nbsp; I &nbsp; Admin</p>

</body>
</html>
```